Packaging Design for High end coffee beans

The name is Cafe de Marvela.

I need this design to be amended you are welcome to design your own too.

We sell high end coffee beans from Colombia this needs to be reflected in the packaging.

The colour is black and Gold. i need the lettering to be fully gold not a fade.

It is to be printed on coffee packaging so the clarity and quality has to be ready for that.

I need Just harvest and Woodland covenant logos added.
Also to be added to the design is:
Single Origin
Traceability
Sustainability

"Awaken you senses" to be added.

I have added some jpegs that i own. you are free to use stock images where appropiate.

Target Market(s)

Coffee Consumers

Requirements
Must have
• Scalable vector files .. whatever images or file design you prodcue mut be able to be printed in high quality
High end quality
Awaken Your Senses needs tl be shown
Logos of just harvest or Wood land covenant to be added
200g weight to be shown
We have 4 beans which need to be shown individually
Velma Nectar
K3 Morandi
Teal Juniper
Altezza Amber
Nice to have
• You are welcome to come up with your own design

```html
<!DOCTYPE html>
<html lang="en">
<head>
<meta charset="utf-8">
<title>Cafe de Marvela – K3 Morandi Packaging</title>
<link rel="stylesheet" href="https://fonts.googleapis.com/css2?family=Josefin+Sans:wght@300;400&display=swap">
<style>
  :root {
    --page: #ffffff;
    --panel: #2b2b2b;
    --band: #1d1d1d;
    --gold: #f6b418;
  }
  * { margin: 0; padding: 0; box-sizing: border-box; }
  html, body {
    width: 1200px;
    height: 1000px;
    overflow: hidden;
    background: var(--page);
  }
  .canvas {
    position: relative;
    width: 1200px;
    height: 1000px;
    font-family: "Josefin Sans", sans-serif;
    color: var(--gold);
  }
  .pack-face {
    position: absolute;
    top: 8px;
    width: 553px;
    height: 982px;
    background: var(--panel);
    overflow: hidden;
  }
  .pack-face--front { left: 30px; }
  .pack-face--back { left: 621px; }

  .pattern-band {
    position: absolute;
    left: 0;
    width: 100%;
    height: 88px;
    background: var(--band);
  }
  .pattern-band--top { top: 0; }
  .pattern-band--bottom { bottom: 0; }

  .centered {
    position: absolute;
    left: 0;
    width: 100%;
    text-align: center;
    white-space: nowrap;
  }

  .brand-name {
    font-weight: 400;
    letter-spacing: 3px;
    text-transform: uppercase;
  }
  .front .brand-name { top: 232px; font-size: 34px; }
  .back .brand-name { top: 138px; font-size: 20px; }

  .tagline {
    font-weight: 300;
    text-transform: uppercase;
  }
  .front .tagline { top: 460px; font-size: 24px; letter-spacing: 6.5px; }
  .back .tagline { top: 236px; font-size: 17px; letter-spacing: 5px; }

  .bean-ornament {
    position: absolute;
    left: 145px;
    top: 680px;
    width: 268px;
    height: 90px;
    background: linear-gradient(90deg, rgba(246,180,24,0.55), var(--gold), rgba(246,180,24,0.55));
    border-radius: 45px;
  }
  .bean-name {
    top: 790px;
    font-size: 28px;
    font-weight: 300;
    letter-spacing: 6px;
    text-transform: uppercase;
  }
  .net-weight {
    top: 870px;
    font-size: 13px;
    letter-spacing: 4px;
    font-weight: 300;
  }

  .story {
    top: 266px;
    font-size: 19px;
    line-height: 27.6px;
    font-weight: 300;
    letter-spacing: 1.2px;
  }
  .maker-name {
    top: 690px;
    font-size: 22px;
    letter-spacing: 5px;
    font-weight: 300;
  }
  .maker-phone {
    top: 726px;
    font-size: 16px;
    letter-spacing: 2px;
  }
  .maker-web {
    top: 756px;
    font-size: 14px;
    letter-spacing: 6px;
    font-weight: 300;
  }
  .cert-badges {
    position: absolute;
    left: 0;
    top: 780px;
    width: 100%;
    height: 72px;
  }
  .origin-note {
    top: 862px;
    font-size: 10.5px;
    line-height: 13px;
    letter-spacing: 3px;
    text-transform: uppercase;
  }
</style>
</head>
<body>
<main class="canvas">

  <section class="pack-face pack-face--front front">
    <div class="pattern-band pattern-band--top" role="img" aria-label="Dark geometric pre-Columbian pattern band"></div>

    <p class="centered brand-name">Cafe de Marvela</p>
    <p class="centered tagline">Awaken your senses</p>

    <div class="bean-ornament" role="img" aria-label="Gold geometric tribal ornament with arrows and triangles"></div>
    <h1 class="centered bean-name">K3 Morandi</h1>
    <p class="centered net-weight">NET WT 200g</p>

    <div class="pattern-band pattern-band--bottom" role="img" aria-label="Dark geometric pre-Columbian pattern band"></div>
  </section>

  <section class="pack-face pack-face--back back">
    <div class="pattern-band pattern-band--top" role="img" aria-label="Dark geometric pre-Columbian pattern band"></div>

    <p class="centered brand-name">Cafe de Marvela</p>
    <p class="centered tagline">Awaken your senses</p>

    <p class="centered story">
      Our Colombian coffee mountains are giving<br>
      birth to our coffee beans, the beans are born in<br>
      coffee families. That have generations of<br>
      tradition in producing coffee. It is this passion,<br>
      love and dedication that our coffee families give<br>
      day to day to each process and step to<br>
      make the best coffee.<br>
      You are not only sipping on the finest coffee you<br>
      are also experiencing a journey into the<br>
      Colombian culture.
    </p>

    <p class="centered maker-name">Café De Marvela</p>
    <p class="centered maker-phone">Tel: 0203 555 0142</p>
    <p class="centered maker-web">www.marvelacafe.com</p>

    <svg class="cert-badges" viewBox="0 0 553 72" role="img" aria-label="Just harvest and Woodland covenant certification badges">
      <circle class="badge badge--just-harvest" cx="222" cy="36" r="30" fill="var(--gold)"/>
      <circle class="badge badge--woodland-covenant" cx="334" cy="36" r="33" fill="var(--gold)"/>
    </svg>

    <p class="centered origin-note">Single origin Colombian coffee beans<br>Roasted and packed in the United Kingdom</p>

    <div class="pattern-band pattern-band--bottom" role="img" aria-label="Dark geometric pre-Columbian pattern band"></div>
  </section>

</main>
</body>
</html>
```